Wedding Ceremony Equipment Hire Business Card

I need a business card design for a new business I created called Vow Outfitters. We hire out Wedding Ceremony equipment and decorations mainly for beach and garden wedding ceremonies that include delivery, set up and dismantle. We do offer DIY Chair Hire as well.
I'd like to have a similar design and colours to our website:
www.vowoutfitters-example.com.au
If possible would like the front to incorporate our information and logo and the back to have two faded example pictures of our wedding ceremonies.
I have attached two photos and our logo. Please let me know if you need a better pic of our logo though.

Target Market(s)

Newly engaged couples, aged 25 and upwards

Industry/Entity Type

Wedding

Contact Information for Business Card

Vow Outfitters
Merel Thorpe
0491 870 264
vowoutfitters@mailbox-example.com
www.social-example.com/VowOutfitters

```html
<!DOCTYPE html>
<html lang="en">
<head>
<meta charset="utf-8">
<title>Vow Outfitters – Business Card</title>
<link rel="stylesheet" href="https://fonts.googleapis.com/css2?family=Cormorant+Garamond:wght@500&family=Open+Sans:wght@400;700&display=swap">
<style>
  :root {
    --backdrop: #eceeed;
    --paper: #f2f6f5;
    --sage: #aecdc5;
    --ink: #262626;
    --silver-dark: #6d6d6d;
    --silver-light: #f4f4f4;
    --photo-garden: #86a368;
    --photo-beach: #c6a679;
    --photo-frame: #ffffff;
  }
  * { box-sizing: border-box; margin: 0; padding: 0; }
  html, body { width: 1200px; height: 1041px; overflow: hidden; }
  body {
    background: var(--backdrop);
    position: relative;
    font-family: "Open Sans", Arial, sans-serif;
    color: var(--ink);
  }
  .card {
    position: absolute;
    width: 461px;
    height: 780px;
    overflow: hidden;
    background: var(--sage);
    box-shadow: 0 2px 8px rgba(0,0,0,0.18);
  }
  .card--front { left: 85px; top: 100px; }
  .card--back { left: 657px; top: 98px; }

  .silver-band {
    position: absolute; left: 0; width: 100%;
    background: linear-gradient(90deg, var(--silver-dark) 0%, #b5b5b5 30%, var(--silver-light) 50%, #b5b5b5 70%, var(--silver-dark) 100%);
  }
  .header-panel { position: absolute; left: 0; width: 100%; background: var(--paper); }

  .card--front .silver-band--top { top: 0; height: 47px; }
  .card--front .header-panel { top: 47px; height: 241px; }
  .card--front .silver-band--bottom { top: 288px; height: 23px; }

  .card--back .silver-band--top { top: 0; height: 47px; }
  .card--back .header-panel { top: 47px; height: 157px; }
  .card--back .silver-band--bottom { top: 204px; height: 22px; }

  .brand-name {
    position: absolute; left: 0; width: 100%;
    text-align: center;
    font-family: "Cormorant Garamond", Georgia, serif;
    font-weight: 500;
    color: var(--ink);
    white-space: nowrap;
  }
  .card--front .brand-name { top: 136px; font-size: 62px; line-height: 1; }
  .card--back .brand-name { top: 100px; font-size: 52px; line-height: 1; }

  .contact-name {
    position: absolute; left: 0; width: 100%; top: 362px;
    text-align: center; font-weight: 700; font-size: 25px;
  }
  .contact-list { position: absolute; left: 30px; top: 437px; list-style: none; }
  .contact-list li {
    display: flex; align-items: center; height: 49px;
    font-size: 20px; white-space: nowrap;
  }
  .contact-list svg { width: 20px; height: 20px; margin-right: 12px; flex: none; }

  .photo {
    position: absolute;
    border: 6px solid var(--photo-frame);
    box-shadow: 0 2px 6px rgba(0,0,0,0.25);
  }
  .photo--garden {
    left: 34px; top: 200px; width: 380px; height: 295px;
    transform: rotate(-4deg);
    background: var(--photo-garden);
  }
  .photo--beach {
    left: 22px; top: 508px; width: 410px; height: 265px;
    transform: rotate(3deg);
    background: var(--photo-beach);
  }
</style>
</head>
<body>
  <section class="card card--front" aria-label="Business card front">
    <div class="silver-band silver-band--top"></div>
    <div class="header-panel"></div>
    <div class="silver-band silver-band--bottom"></div>
    <div class="brand-name">Vow Outfitters</div>

    <div class="contact-name">Merel Thorpe</div>
    <ul class="contact-list">
      <li>
        <svg viewBox="0 0 20 20" aria-hidden="true"><path d="M5 2 L8 2 L9 6 L7 8 C8 11 10 13 12 14 L14 12 L18 13 L18 16 C18 17 17 18 16 18 C9 18 2 11 2 4 C2 3 3 2 5 2 Z" fill="none" stroke="#262626" stroke-width="1.6" stroke-linejoin="round"/></svg>
        0491 870 264
      </li>
      <li>
        <svg viewBox="0 0 20 20" aria-hidden="true"><rect x="2" y="5" width="16" height="11" fill="none" stroke="#262626" stroke-width="1.5"/><path d="M2 5 L10 11 L18 5" fill="none" stroke="#262626" stroke-width="1.5"/></svg>
        vowoutfitters@mailbox-example.com
      </li>
      <li>
        <svg viewBox="0 0 20 20" aria-hidden="true"><circle cx="10" cy="10" r="8" fill="none" stroke="#262626" stroke-width="1.5"/><ellipse cx="10" cy="10" rx="3.5" ry="8" fill="none" stroke="#262626" stroke-width="1.3"/><line x1="2" y1="10" x2="18" y2="10" stroke="#262626" stroke-width="1.3"/></svg>
        www.vowoutfitters-example.com.au
      </li>
      <li>
        <svg viewBox="0 0 20 20" aria-hidden="true"><rect x="2" y="2" width="16" height="16" rx="2" fill="none" stroke="#262626" stroke-width="1.5"/></svg>
        www.social-example.com/VowOutfitters
      </li>
    </ul>
  </section>

  <section class="card card--back" aria-label="Business card back">
    <div class="silver-band silver-band--top"></div>
    <div class="header-panel"></div>
    <div class="silver-band silver-band--bottom"></div>
    <div class="brand-name">Vow Outfitters</div>

    <div class="photo photo--garden" role="img" aria-label="Photo of a garden wedding ceremony setup with white chairs and an aisle runner on a lawn"></div>
    <div class="photo photo--beach" role="img" aria-label="Photo of a beach wedding ceremony setup with rows of white chairs along a sandy aisle"></div>
  </section>
</body>
</html>
```